ROLL-ON-VERANDA Business Card Design

Please do not submit more than one design per designer. Both the front and the back must be submitted as a single design. Please use all of the attached files to design a two-sided business card. Do not use tiny text that is hard to read. Do not put text or images too close to the edges where it might get cut off during printing. The card should be horizontal. Please do not send me the same design that I attached showing the business information. Be creative.

One file is marked as the primary logo for company. Other files are marked as secondary. All logos should be incorporated into the design with a focus on the primary one being bigger.

```html
<!DOCTYPE html>
<html lang="en">
<head>
<meta charset="utf-8">
<title>ROLL-ON-VERANDA Business Card</title>
<link rel="stylesheet" href="https://fonts.googleapis.com/css2?family=Russo+One&family=Lato:wght@400;700&display=swap">
<style>
  :root {
    --backdrop: #909090;
    --card: #ffffff;
    --ink: #0d0d0d;
    --text: #1a1a1a;
    --muted: #333333;
    --illus-light: #d9d9d9;
    --illus-dark: #3a3a3a;
    --badge-navy: #1b2a5c;
    --badge-gold: #c9a23a;
    --badge-red: #d22630;
    --badge-blue: #1f5fa8;
  }
  * { box-sizing: border-box; margin: 0; padding: 0; }
  html, body { width: 1200px; height: 1200px; overflow: hidden; }
  body { background: var(--backdrop); position: relative; font-family: "Lato", sans-serif; }

  .card {
    position: absolute;
    left: 281px;
    width: 641px;
    height: 366px;
    background: var(--card);
    border-radius: 18px;
    overflow: hidden;
  }
  .card--front { top: 195px; }
  .card--back { top: 639px; }

  /* front */
  .front-wave { position: absolute; left: 0; top: 0; width: 641px; height: 366px; }
  .boat-illustration {
    position: absolute;
    left: 46px; top: 107px; width: 297px; height: 142px;
    background: linear-gradient(160deg, var(--illus-light), var(--illus-dark));
    border-radius: 40px 60px 90px 20px;
  }
  .owner-name {
    position: absolute; right: 41px; top: 34px;
    font-family: "Russo One", sans-serif;
    font-size: 28px; letter-spacing: 0.5px; color: var(--ink);
    white-space: nowrap;
  }
  .credentials {
    position: absolute; right: 41px; top: 64px;
    list-style: none; text-align: right;
    font-size: 17px; line-height: 20.5px; color: var(--text); letter-spacing: 0.3px;
  }
  .contacts {
    position: absolute; right: 41px; top: 154px;
    list-style: none; text-align: right; color: var(--muted);
  }
  .contacts li { display: flex; justify-content: flex-end; align-items: center; gap: 7px; height: 22px; font-size: 14.5px; }
  .contacts li.phone { font-size: 17.5px; color: var(--text); height: 26px; margin-bottom: 1px; }
  .contacts svg { width: 12px; height: 12px; fill: var(--ink); }
  .tagline {
    position: absolute; left: 0; right: 0; top: 302px;
    text-align: center; color: #fff;
    font-family: "Russo One", sans-serif; font-size: 12.5px; line-height: 16px; letter-spacing: 0.6px;
    padding-left: 18px;
  }

  /* back */
  .mark-illustration {
    position: absolute; left: 160px; top: 50px; width: 323px; height: 131px;
    background: radial-gradient(ellipse at 50% 55%, var(--illus-dark), var(--illus-light) 75%, #fff);
    border-radius: 50%;
  }
  .wordmark {
    position: absolute; left: 0; right: 0; top: 182px; text-align: center;
    font-family: "Russo One", sans-serif; font-size: 34px; color: var(--ink); line-height: 40px;
  }
  .wordmark-tld {
    position: absolute; right: 156px; top: 216px;
    font-family: "Russo One", sans-serif; font-size: 18px; color: var(--ink);
  }
  .badges { position: absolute; left: 0; top: 249px; width: 641px; height: 84px; }
  .badge { position: absolute; top: 0; width: 84px; height: 84px; border-radius: 50%; }
  .badge--coast { left: 45px; background: var(--badge-navy); border: 4px solid #fff; box-shadow: 0 0 0 2px var(--badge-navy); }
  .badge--school { left: 200px; background: var(--ink); border: 5px solid var(--badge-gold); }
  .badge--veteran { left: 356px; background: var(--badge-red); border: 6px solid var(--badge-navy); }
  .badge--instructor { left: 506px; background: var(--badge-blue); border: 6px solid #5fb3d6; }
</style>
</head>
<body>

<section class="card card--front">
  <svg class="front-wave" viewBox="0 0 641 366" aria-hidden="true">
    <path d="M0 209 C 170 280, 420 300, 641 229 L641 366 L0 366 Z" fill="var(--ink)"/>
    <path d="M60 245 C 220 300, 450 300, 600 272 C 450 292, 230 292, 60 245 Z" fill="#fff"/>
  </svg>
  <div class="boat-illustration" role="img" aria-label="Black and white illustration of a cabin motorboat cruising on the water"></div>

  <h1 class="owner-name">CAPTAIN DALTON R.WEXLEY</h1>
  <ul class="credentials">
    <li>USCG Licensed Master Captain</li>
    <li>CSBA Certified Instructor</li>
    <li>Veteran Owned Business</li>
    <li>Graduate Degree</li>
  </ul>
  <ul class="contacts">
    <li class="phone">(727) 555-0148
      <svg viewBox="0 0 24 24"><path d="M6.6 10.8a15 15 0 0 0 6.6 6.6l2.2-2.2c.3-.3.7-.4 1-.2 1.1.4 2.3.6 3.6.6.6 0 1 .4 1 1V20c0 .6-.4 1-1 1A17 17 0 0 1 3 4c0-.6.4-1 1-1h3.5c.6 0 1 .4 1 1 0 1.3.2 2.5.6 3.6.1.3 0 .7-.2 1z"/></svg>
    </li>
    <li>service@rollonveranda.com
      <svg viewBox="0 0 24 24"><path d="M2 5h20v14H2z M2 5l10 8 10-8" fill="var(--ink)" stroke="#fff" stroke-width="1.6"/></svg>
    </li>
    <li>Roll-On-Veranda.com
      <svg viewBox="0 0 24 24"><circle cx="12" cy="12" r="10"/><path d="M7 8c2 0 3 1 3 3s2 2 2 4-1 3-1 4M15 5c-1 2 0 3 2 3s2 2 3 3" stroke="#fff" stroke-width="1.6" fill="none"/></svg>
    </li>
  </ul>

  <p class="tagline">PROVIDING HANDS-ON BOAT TRAINING, CAPTAINING SERVICES &amp;<br>DELIVERIES IN THE PINELLAS COUNTY AREA.</p>
</section>

<section class="card card--back">
  <div class="mark-illustration" role="img" aria-label="Illustration of a cabin motorboat with a sweeping wake line"></div>
  <div class="wordmark">ROLL-ON-VERANDA</div>
  <div class="wordmark-tld">.COM</div>
  <div class="badges">
    <div class="badge badge--coast" role="img" aria-label="Licensed captain badge"></div>
    <div class="badge badge--school" role="img" aria-label="Boat training and charters badge"></div>
    <div class="badge badge--veteran" role="img" aria-label="Veteran owned business verified badge"></div>
    <div class="badge badge--instructor" role="img" aria-label="Safe boating council instructor badge"></div>
  </div>
</section>

</body>
</html>
```